Sophisticated & Clean Comedy Show Flyer

Pale Harbor Entertainment, a talent management company, is producing a showcase to introduce their comedians to the industry. The design should be clean and sophisticated and introduce a graphical element that evokes comedy, without being cheesy.

I have attached the following files:
* Pale Harbor Logo - file #1
* Copy for flyer - file #2
* textured business card for Pale Harbor Entertainment for design reference - file #3
* example of a comedy flyer with graphic and texture that is clean and sophisticated and fun. - file #4

Industry/Entity Type

Entertainment Industry

Font styles to use
Sans Serif

Colors
000000
ffffff
e8e8e8

Requirements
Must have
• Logo ad all the content listed in the file #2
Nice to have
• A graphical element that evokes comedy that is not generic or cheesy
• I don't mind accent color on the flyer - but overall it should be clean look

```html
<!DOCTYPE html>
<html lang="en">
<head>
<meta charset="utf-8">
<title>Pale Harbor Entertainment – Comedy Showcase</title>
<link href="https://fonts.googleapis.com/css2?family=Oswald:wght@400;500;700&display=swap" rel="stylesheet">
<style>
  :root {
    --ink: #000000;
    --paper: #ffffff;
    --mist: #e8e8e8;
    --lip: #e98f79;
    --lip-deep: #d4705c;
    --wall: #f1f0ee;
    --wall-shade: #dcdad6;
  }
  * { margin: 0; padding: 0; box-sizing: border-box; }
  html, body { width: 851px; height: 1200px; overflow: hidden; }
  body {
    position: relative;
    background: linear-gradient(180deg, #f4f4f4 0%, var(--mist) 100%);
    font-family: "Oswald", sans-serif;
    color: var(--ink);
  }
  .brand {
    position: absolute; top: 18px; left: 0; width: 851px;
    text-align: center; line-height: 1;
  }
  .brand-name {
    display: inline-block;
    font-size: 62px; font-weight: 700; letter-spacing: 2px;
    text-transform: uppercase;
  }
  .brand-sub {
    display: block; margin-top: 4px;
    font-size: 22px; font-weight: 500; letter-spacing: 4px;
    text-transform: uppercase;
  }
  .title {
    position: absolute; top: 190px; left: 0; width: 851px;
    text-align: center; font-size: 56px; font-weight: 700;
    letter-spacing: 1px; text-transform: uppercase;
  }
  .mouth-art {
    position: absolute; top: 285px; left: 0; width: 380px; height: 420px;
    background: radial-gradient(ellipse at 35% 50%, var(--lip) 0%, var(--lip-deep) 100%);
    border-radius: 0 60% 55% 0 / 0 50% 50% 0;
  }
  .date {
    position: absolute; top: 420px; left: 40px; width: 300px;
    text-align: center; color: var(--paper); text-transform: uppercase;
    line-height: 1.05;
  }
  .date-day { font-size: 46px; font-weight: 700; display: block; }
  .date-month { font-size: 40px; font-weight: 700; display: block; }
  .date-times { font-size: 30px; font-weight: 500; display: block; margin-top: 6px; text-transform: none; }
  .host {
    position: absolute; top: 300px; left: 470px; width: 320px;
    text-align: center; line-height: 1.1;
  }
  .host-label { font-size: 32px; font-weight: 700; display: block; }
  .host-name { font-size: 34px; font-weight: 700; display: block; text-transform: uppercase; margin-top: 6px; }
  .host-credit { font-size: 28px; font-weight: 500; display: block; }
  .featuring {
    position: absolute; top: 450px; left: 418px; width: 420px;
  }
  .featuring-label { font-size: 40px; font-weight: 700; display: block; margin-bottom: 6px; }
  .lineup { list-style: none; font-size: 22px; font-weight: 500; line-height: 1.35; text-transform: uppercase; }
  .lineup span { text-transform: none; }
  .rule {
    position: absolute; top: 715px; left: 0; width: 851px; height: 3px;
    background: var(--ink);
  }
  .venue {
    position: absolute; top: 738px; left: 0; width: 851px;
    text-align: center; font-size: 40px; font-weight: 700;
    text-transform: uppercase; letter-spacing: 0.5px;
  }
  .photo {
    position: absolute; top: 810px; left: 0; width: 851px; height: 390px;
    background: linear-gradient(180deg, var(--wall) 0%, var(--wall-shade) 100%);
  }
</style>
</head>
<body>
  <header class="brand">
    <span class="brand-name">Pale Harbor</span>
    <span class="brand-sub">Entertainment</span>
  </header>

  <h1 class="title">Comedy Showcase</h1>

  <div class="mouth-art" role="img" aria-label="Illustration of a wide laughing mouth in coral tones"></div>
  <p class="date">
    <span class="date-day">Monday</span>
    <span class="date-month">November 16th</span>
    <span class="date-times">Doors 7PM<br>Show 7:30PM</span>
  </p>

  <div class="host">
    <span class="host-label">Hosted by</span>
    <span class="host-name">Big Ray<br>Hollister</span>
    <span class="host-credit">(Laugh Channel)</span>
  </div>

  <section class="featuring">
    <span class="featuring-label">Featuring</span>
    <ul class="lineup">
      <li>Terry Wollett <span>(Laugh Channel, Beat2)</span></li>
      <li>Marcus DelBee <span>(Vista TV, Crest)</span></li>
      <li>Tamsin Joaquin <span>(Vista TV)</span></li>
      <li>Corey Balmont <span>(Current, Vista TV)</span></li>
      <li>Mitchell Brennan <span>(Hudson Comedy Festival)</span></li>
    </ul>
  </section>

  <div class="rule"></div>
  <p class="venue">Linwood 118 W 9th Street, NY, NY 10014</p>

  <div class="photo" role="img" aria-label="Photo of a laughing woman hanging from a ledge against a pale wall"></div>
</body>
</html>
```